Health care finance company startup website design

This design brief is for Ledger Loom, a small start-up company dealing with an online health care (initially dental targeted with plans for medical market) financial suite of tools. My business partners and I are looking to have a website developed for our business model.

We have developed a professional logo and would like it incorporated into the site. We are open to modifications on the logo if needed to accomplish the right design.

Our concept is a clean, simple design with a professional polish and very up-to-date web presence. The functionality of the site is simple yet powerful and we would like it’s design to complement that (including anticipated css3/html5 effects for an added dimension of UI polish).

We would like to see a design mockup of the functional elements of our site as our home page. We would also be very interested to see how your design would flow into the other pages such as search for a loan, create a payment plan, make a payment, sign in, registration, contact us and learn more.

Regarding Functional Elements:

-Simplicity is king.

-The three main functions of the site are the focus. They will operate via a series of API’s to webservices on the back-end, making the front end field focused, though we hope to have it feel friendly and simple.
-Search for a loan
-Create a payment plan
-Make a payment

Other functions of the site include:

-Sign in module
-We plan to support Kindred Link, Vortal Verify and PassGate so incorporating design for those options is a plus.

-Registration module
-Two service levels clients can register for, loans only or loans & payments
-The registration process should be divided into sections with navigation back and forth until a confirmation final screen with pdf generations and remaining “to-do items” listed.
-The registration information will be saved in our database and also auto-populate fields for PDF’s that will be generated from templates.
-The registration will send a confirmation email and support PassGate, Vortal Verify and Kindred Link, so designs should take these programmatic features into account.

-Contact us
-This will emphasize digital forms of communication (email and form submitted contact request).

-Learn more
-Explanations/faqs/tutorials
-This will contain video demonstrations/screencasts of key functions of website features

Regarding Design Elements:
-We want to be “wow’d” and don’t mind a surprise that redefines what we thought we liked regarding design.
-The following examples indicate some of the color schemes we like and design elements we hope to incorporate.
-We also recognize there is no substitute for creativity and originality.

Favorite Website Design Examples:

http://www.joggingwithmarla.example/
HD backgrounds are a plus.
These colors are great.
The bright splashes of blue, red and orange combined with black in these shades.
A predominant background of whitesmoke or beige.

https://tillbrook.example/
The HD backgrounds are sharp.
The look is very clean (though it has a slight Pearfield computers imitation).
The left to right “scrolling” is preferable to vertical scrolling.
Very pleasing to the eye.

http://www.gravelpathworks.example/
Again, use of bright, vibrant HD graphics is exceptional.
The left to right scrolling navigation is slick and likely how we would like our services to flow.

http://buzzing.visitlakeshore.example/
Love the look, feel and concepts in this site’s design
Especially colors and “photography” elements.
Updates

We've seen a few common themes in various designs submitted so far and want to add a few suggestions as we enter the final week of our design contest.

We do not want any photos of healthcare professionals or close-ups of people (families or couples or individuals).  Although we are a health care company we don't want to fall into a cliche feel for our site.  Instead we would like either objects or abstract images that have depth and are high definition, spanning from edge to edge of the width of the screen. 

We prefer shades of grey for the base color scheme with highlights of bright colors.  Please refer to the examples on the brief and use those as the best guide of what we want.  Even SketchHive's color scheme is closer to what we want than some of the submissions, so please take note of the "shades of grey" with splashes of bright accent colors.

We love the horizontal navigation bar like that seen in the gravel-path works site and anticipate our final product using a similar transition between the functions of the site.

Good luck to you all.  We are still looking for that WOW factor and hoping to see something original, that breaks the traditional mold and has a feel like the examples posted.  

Industry/Entity Type

Communication

```html
<!DOCTYPE html>
<html lang="en">
<head>
<meta charset="utf-8">
<title>Ledger Loom – Home</title>
<link href="https://fonts.googleapis.com/css2?family=Gelasio:ital,wght@0,400;0,700;1,700&family=Open+Sans:wght@400;600&family=Ubuntu:wght@300;400;500&display=swap" rel="stylesheet">
<style>
:root{
  --navy:#141d45;
  --navy-deep:#0f1838;
  --teal:#14b5c8;
  --gold-top:#ffd514;
  --gold-bottom:#ffb300;
  --ink:#1d2230;
  --body:#3d4654;
  --muted:#5d6670;
  --rule:#8fcfd6;
  --sky-top:#e0fcfd;
  --sky-bottom:#a8d4f0;
  --footer:#242424;
  --orange:#f0a400;
  --heading:"Gelasio",Georgia,serif;
  --ui:"Ubuntu",Arial,sans-serif;
  --text:"Open Sans",Arial,sans-serif;
}
*{box-sizing:border-box;margin:0;padding:0}
html,body{width:966px;height:1200px;overflow:hidden}
body{position:relative;background:linear-gradient(180deg,var(--sky-top) 0%,#cdeefa 45%,var(--sky-bottom) 100%);font-family:var(--text);color:var(--body);border-top:4px solid #0e1f33}
.abs{position:absolute}
a{color:inherit}

/* header */
.brand{left:110px;top:35px;display:flex;align-items:center;gap:14px}
.brand-mark{width:51px;height:51px;border-radius:7px;background:var(--navy)}
.brand-name{font-family:var(--ui);font-weight:300;font-size:37px;color:#3a3f47;letter-spacing:.5px}
.call{right:106px;top:44px;font-family:var(--ui);font-size:19px;color:#111;letter-spacing:-.3px}
.call b{font-weight:500}
.search{left:675px;top:75px;width:185px;height:23px;border-radius:11px;border:1px solid #c8d0d4;background:linear-gradient(#fdfdfd,#e9ecee);display:flex;align-items:center;gap:8px;padding-left:8px;font-family:var(--ui);font-size:11px;color:#555}

/* nav */
.main-nav{left:93px;top:113px;width:788px;height:44px;border-radius:11px;background:linear-gradient(var(--gold-top),var(--gold-bottom));border:1px solid #ffe36a;box-shadow:inset 0 1px 0 #fff3a0}
.main-nav span{position:absolute;top:0;line-height:42px;font-family:var(--ui);font-size:11.5px;color:var(--ink);transform:translateX(-50%);white-space:nowrap}
.main-nav .current{top:11px;line-height:21px;padding:0 8px;background:#1f1f1f;color:#fff;border-radius:3px}

/* hero */
.hero{left:93px;top:170px;width:789px;height:292px;border:3px solid var(--teal);border-radius:3px;overflow:hidden}
.hero-photo{position:absolute;inset:0;background:radial-gradient(ellipse at 72% 40%,#fff2c4 0%,#f7c86a 25%,#e99a22 55%,#c86e10 100%)}
.hero-shadow{left:110px;top:460px;width:756px;height:24px;border-radius:50%;background:radial-gradient(ellipse at 50% 0,rgba(40,60,80,.35),rgba(40,60,80,0) 70%)}
.signup{left:26px;top:28px;width:315px;height:237px;border:1px solid rgba(120,90,40,.5);border-radius:4px;background:rgba(255,238,196,.6);overflow:hidden}
.signup h3{height:42px;background:var(--navy);color:#fff;font-family:var(--ui);font-weight:400;font-size:19px;line-height:44px;padding-left:12px}
.field{position:absolute;left:0;display:flex;align-items:center;width:298px;justify-content:flex-end;gap:8px}
.field label{font-family:var(--ui);font-size:11.5px;color:#2c2c2c}
.field i{display:block;width:178px;height:28px;background:#f1f1f1;border:1px solid #3b8fa6}
.envelope{position:absolute;left:25px;top:64px}
.signup-btn{position:absolute;left:58px;top:195px;width:198px;height:27px;background:linear-gradient(#6fcdeb,#2b9ccc);color:#fff;font-family:var(--ui);font-size:12px;text-align:center;line-height:27px}

/* left column */
.section-title{font-family:var(--heading);font-weight:400;color:var(--navy-deep);font-size:25px}
.welcome-title{left:94px;top:510px}
.welcome-text{left:97px;top:556px;width:315px;font-size:9.2px;line-height:11.3px}
.welcome-photo{left:427px;top:557px;width:185px;height:88px;border:3px solid #fff;border-radius:8px;background:linear-gradient(120deg,#d8dfe8,#9fb2c4 55%,#4a78a6);box-shadow:0 1px 3px rgba(0,0,0,.2)}
.btn-gold{background:linear-gradient(var(--gold-top),var(--gold-bottom));border:1px solid #f0b000;color:#222;font-family:Arial,sans-serif;font-size:9.5px;text-align:center;font-style:italic}
.welcome-more{left:97px;top:671px;width:70px;height:19px;line-height:17px}
.rule{height:1px;background:var(--rule)}
.rule-1{left:103px;top:718px;width:506px}
.feature{left:103px;top:736px;width:511px;height:210px;background:var(--navy);border:1px solid var(--teal);border-radius:6px;padding:10px 12px;color:#e6e9f2}
.feature h3{font-family:var(--heading);font-style:italic;font-weight:700;font-size:20px;color:#fff;margin-bottom:4px}
.feature p{font-size:9.4px;line-height:12.9px;margin-bottom:17px}
.feature a{font-size:9.7px;position:absolute;left:12px;top:183px}
.rule-2{left:103px;top:972px;width:506px}
.testi-title{left:95px;top:986px}
.testi-photo{left:105px;top:1028px;width:91px;height:85px;background:linear-gradient(160deg,#f4f6f8,#c9d6e2 60%,#8aa4bf)}
.testi-text{left:212px;top:1029px;width:402px;font-size:9.4px;line-height:12.9px;color:var(--muted)}

/* right column */
.col-rule{left:625px;top:483px;width:1px;height:652px;background:#b7d8e2}
.login-title{left:643px;top:510px}
.login-row{left:643px;display:flex;align-items:center;font-family:var(--text);font-size:10.5px;color:#222}
.login-row label{width:61px}
.login-row i{display:block;width:152px;height:18px;background:#fff;border:1px solid #bfc6ca}
.remember{left:705px;top:607px;display:flex;align-items:center;gap:5px;font-family:var(--heading);font-size:7.5px;color:#333}
.tick{width:12px;height:12px;background:#e9eeee;border:1px solid #b5c0c0}
.submit{left:785px;top:604px;width:69px;height:18px;line-height:16px;font-family:var(--heading);font-style:normal;font-size:11px;color:#6b4a00}
.login-links{left:700px;top:632px;font-family:var(--heading);font-size:9.5px;color:#1b1b2a}
.rule-3{left:642px;top:673px;width:231px}
.topics-title{left:642px;top:687px}
.topic{left:642px;font-family:var(--heading);font-size:9.5px;line-height:13.5px;color:#13203f}
.topic span,.topic a{display:block}
.topics-more{left:644px;top:848px;font-family:Arial,sans-serif;font-size:9.5px;color:var(--orange)}
.rule-4{left:642px;top:878px;width:231px}
.support{left:641px;top:924px;width:238px;height:103px;border:1px solid #cfd6da;border-radius:5px;background:linear-gradient(#ffffff,#e7eaec)}
.support-photo{left:785px;top:906px;width:94px;height:121px;border-radius:40px 5px 5px 0;background:linear-gradient(180deg,#e8d2c0,#6a5a52 55%,#1e1e22)}
.support-big{left:657px;top:934px;font-family:var(--heading);font-size:32px;color:#111}
.support-small{left:678px;top:969px;font-family:var(--ui);font-size:15px;color:#111}
.support-btn{left:666px;top:1000px;width:71px;height:19px;line-height:17px;font-style:normal}
.accept{left:644px;top:1051px;font-family:var(--text);font-size:16px;color:#222}
.cards{left:644px;top:1085px;display:flex;gap:6px}
.cards span{width:42px;height:28px;border:1px solid #c9d4dc;background:#fff;font-family:var(--text);font-weight:600;font-size:7px;color:var(--navy);display:flex;align-items:center;justify-content:center}

/* footer */
.site-footer{left:0;top:1133px;width:966px;height:67px;background:var(--footer);color:#fff;font-family:var(--text);font-size:9.5px}
.site-footer nav span{position:absolute;top:26px}
.copy{position:absolute;right:93px;top:26px;font-size:8.5px}
.copy a{color:#ffc21a}
</style>
</head>
<body>

<header>
  <div class="abs brand"><span class="brand-mark"></span><span class="brand-name">LEDGER LOOM</span></div>
  <div class="abs call"><b>Call Now:</b> 0800-5512-930</div>
  <div class="abs search">
    <svg width="12" height="12" viewBox="0 0 12 12"><circle cx="5" cy="5" r="3.6" fill="none" stroke="#111" stroke-width="1.8"/><line x1="7.6" y1="7.6" x2="11" y2="11" stroke="#111" stroke-width="2"/></svg>
    SEARCH
  </div>
</header>

<nav class="abs main-nav">
  <span class="current" style="left:62px">HOMEPAGE</span>
  <span style="left:144px">ABOUT US</span>
  <span style="left:228px">LOAN</span>
  <span style="left:348px">CREATE&nbsp; A PAYMENT PLAN</span>
  <span style="left:495px">MAKE A PAYMENT</span>
  <span style="left:610px">LEARN MORE</span>
  <span style="left:718px">CONTACT US</span>
</nav>

<section class="abs hero">
  <div class="hero-photo" role="img" aria-label="Warm golden abstract backdrop with bright bokeh light"></div>
  <form class="abs signup">
    <h3>Signup</h3>
    <svg class="envelope" width="46" height="44" viewBox="0 0 46 44"><rect x="2" y="14" width="42" height="28" rx="2" fill="#ffcf3a" stroke="#d99a00"/><path d="M2 16 L23 32 L44 16" fill="none" stroke="#d99a00" stroke-width="1.5"/><rect x="10" y="2" width="24" height="20" fill="#f4f8ff" stroke="#9ab" transform="rotate(-12 22 12)"/></svg>
    <div class="field" style="top:78px"><label>Email:</label><i></i></div>
    <div class="field" style="top:114px"><label>Create Password:</label><i></i></div>
    <div class="field" style="top:150px"><label>Confirm Password:</label><i></i></div>
    <div class="signup-btn">Sign Up For Ledger Loom</div>
  </form>
</section>
<div class="abs hero-shadow"></div>

<main>
  <h2 class="abs section-title welcome-title">Welcome to our Ledger Loom</h2>
  <p class="abs welcome-text">Lorem Ipsum is simply dummy text of the printing and typesetting industry. Lorem Ipsum has been the industry's standard dummy text ever since the 1500s, when an unknown printer took a galley of type and scrambled it to make a type specimen book. It has survived not only five centuries, but also the leap into electronic typesetting, remaining essentially unchanged. It was popularised in the 1960s with the release of Letterform sheets containing Lorem Ipsum passages, and more recently with desktop publishing software like Pagewright Studio including versions of Lorem Ipsum.</p>
  <div class="abs welcome-photo" role="img" aria-label="Clinic scene of a patient receiving a check-up"></div>
  <div class="abs btn-gold welcome-more">Read More</div>
  <div class="abs rule rule-1"></div>

  <article class="abs feature">
    <h3>Implant Denistry</h3>
    <p>Lorem Ipsum is simply dummy text of the printing and typesetting industry. Lorem Ipsum has been the industry's standard dummy text ever since the 1500s, when an unknown printer took a galley of type and scrambled it to make a type specimen book. It has survived not only five centuries, but also the leap into electronic typesetting, remaining essentially unchanged. It was popularised in the 1960s with the release of Letterform sheets containing Lorem Ipsum passages, and more recently with desktop publishing software like Pagewright Studio including versions of Lorem Ipsum.</p>
    <p>Lorem Ipsum is simply dummy text of the printing and typesetting industry. Lorem Ipsum has been the industry's standard dummy text ever since the 1500s, when an unknown printer took a galley of type and scrambled it to make a type specimen book. It has survived not only five centuries, but also the leap</p>
    <a href="#">Read More</a>
  </article>
  <div class="abs rule rule-2"></div>

  <h2 class="abs section-title testi-title">Our Testimonials</h2>
  <div class="abs testi-photo" role="img" aria-label="Group of smiling clinic staff"></div>
  <p class="abs testi-text">Lorem Ipsum is simply dummy text of the printing and typesetting industry. Lorem Ipsum has been the industry's standard dummy text ever since the 1500s, when an unknown printer took a galley of type and scrambled it to make a type specimen book. It has survived not only five centuries, but also the leap into electronic typesetting, remaining essentially unchanged. It was popularised in the 1960s with the release of Letterform sheets containing Lorem Ipsum passages, and more recently with desktop publishing software like Pagewright Studio including versions of Lorem Ipsum.</p>
</main>

<aside>
  <div class="abs col-rule"></div>
  <h2 class="abs section-title login-title">Login Form</h2>
  <div class="abs login-row" style="top:554px"><label>Username:</label><i></i></div>
  <div class="abs login-row" style="top:578px"><label>Password:</label><i></i></div>
  <div class="abs remember"><span class="tick"><svg width="10" height="10" viewBox="0 0 10 10"><path d="M1.5 5 L4 7.5 L8.5 2" fill="none" stroke="#2a9a3a" stroke-width="1.8"/></svg></span>Remember Me</div>
  <div class="abs btn-gold submit">Submit</div>
  <div class="abs login-links"><a href="#">Forget Password?</a> &nbsp;|&nbsp; <a href="#">New User Signup</a></div>
  <div class="abs rule rule-3"></div>

  <h2 class="abs section-title topics-title">Latest Topics</h2>
  <div class="abs topic" style="top:732px"><span><u>12.02.12</u></span><a href="#">Lorem ipsum Dolor smit concentrator</a><a href="#">apispisinf elite Nulla et mauris.</a></div>
  <div class="abs topic" style="top:794px"><span><u>22.02.12</u></span><a href="#">Lorem ipsum Dolor smit concentrator</a><a href="#">apispisinf elite Nulla et mauris.</a></div>
  <a class="abs topics-more" href="#">Read More</a>
  <div class="abs rule rule-4"></div>

  <div class="abs support"></div>
  <div class="abs support-photo" role="img" aria-label="Support agent wearing a headset"></div>
  <div class="abs support-big">Online</div>
  <div class="abs support-small">Support</div>
  <div class="abs btn-gold support-btn">Click here</div>

  <div class="abs accept">We Proudly Accept</div>
  <div class="abs cards"><span>Veyra</span><span>Crestcard</span><span>Novapay</span><span>Amberline</span><span>Paywell</span></div>
</aside>

<footer class="abs site-footer">
  <nav>
    <span style="left:114px">Home</span>
    <span style="left:172px">About Us</span>
    <span style="left:243px">Services</span>
    <span style="left:309px">News &amp; Events</span>
    <span style="left:402px">Customer Centre</span>
    <span style="left:505px">Contact Us</span>
  </nav>
  <div class="copy">All Rights Reserved- © 2010 - 2011 <a href="#">Ledger Loom</a></div>
</footer>

</body>
</html>
```